Award winning pet photographer needs business card and letterhead

Business card and letterhead for our Pet photography business. We specialize in studio portraits of dogs.

Target Market(s)

Wealthy and middle class dog owners who would like photos of their dogs as wall art.

Industry/Entity Type

Portrait Photography

Contact Information for Business Card

Our business name is Tails of Glee Pet Photography. Would be good to include dog and a heart, bright colours and a modern design

Font styles to use
Sans Serif

Colors
f04a50
f68d4d
faa54b
33a6d7
33b8a4
abd036

Requirements
Must have
• Business name: Tails of Glee Pet Photography
• Phone number: 0437 560914
• Email: marcus@kfstudio.com.au
• Website:www.tailsofglee.com.au
• Photographer: Marcus Fenwick
Nice to have
• In Addition letterhead should include
• Studio address 27 Wren Close, Marrowdale 6015
• Postal Address 9 Harlow St, East Marrowdale 6015

```html
<!DOCTYPE html>
<html lang="en">
<head>
<meta charset="utf-8">
<title>Tails of Glee Pet Photography – Business Card</title>
<link href="https://fonts.googleapis.com/css2?family=Arimo:wght@400;700&display=swap" rel="stylesheet">
<style>
  :root {
    --stage-dark: #2f2f2f;
    --stage-light: #555555;
    --brand-blue: #30a6d9;
    --brand-teal: #33b8a4;
    --paper: #ffffff;
    --divider: rgba(255,255,255,0.75);
  }
  * { margin: 0; padding: 0; box-sizing: border-box; }
  html, body { width: 999px; height: 1200px; overflow: hidden; }
  body {
    font-family: "Arimo", Arial, sans-serif;
    background: radial-gradient(ellipse at center, var(--stage-light) 0%, #484848 55%, var(--stage-dark) 100%);
    position: relative;
  }
  .card {
    position: absolute;
    left: 43px;
    width: 913px;
    height: 521px;
    overflow: hidden;
  }
  .card--front { top: 72px; background: var(--paper); }
  .card--back { top: 622px; height: 520px; background: var(--brand-blue); }

  .card__wave { position: absolute; left: 0; top: 0; width: 913px; height: 521px; }

  .brand { position: absolute; display: flex; align-items: center; }
  .brand__mark { border-radius: 50%; flex: none; }
  .brand__name { font-weight: 400; line-height: 1.12; }
  .brand__name span { display: block; }

  .card--front .brand { left: 227px; top: 70px; }
  .card--front .brand__mark { width: 140px; height: 140px; background: var(--brand-blue); margin-right: 20px; }
  .card--front .brand__name { color: var(--brand-blue); font-size: 40px; }

  .card--back .brand { left: 200px; top: 180px; }
  .card--back .brand__mark { width: 150px; height: 150px; background: var(--paper); margin-right: 28px; }
  .card--back .brand__name { color: var(--paper); font-size: 42px; }

  .contact { position: absolute; color: var(--paper); font-size: 22px; line-height: 30.5px; }
  .contact__name { font-weight: 700; font-size: 29px; line-height: 36px; }
  .contact__role { margin-bottom: 8px; }
  .contact--person { left: 39px; top: 324px; }
  .contact--address { left: 527px; top: 340px; }
  .contact__label { font-weight: 700; }

  .contact-divider {
    position: absolute; left: 439px; top: 351px;
    width: 2px; height: 137px;
    background: linear-gradient(to bottom, transparent, var(--divider) 20%, var(--divider) 80%, transparent);
  }
</style>
</head>
<body>
  <section class="card card--front">
    <svg class="card__wave" viewBox="0 0 913 521" aria-hidden="true">
      <path d="M0 288 C 180 318, 420 330, 560 318 C 700 306, 830 290, 913 272 L913 521 L0 521 Z" fill="#30a6d9"/>
      <path d="M365 316 C 560 312, 760 290, 913 262 L913 284 C 760 306, 560 320, 365 316 Z" fill="#33b8a4"/>
      <path d="M365 316 C 560 320, 760 306, 913 284 L913 289 C 760 311, 560 324, 365 316 Z" fill="#ffffff"/>
    </svg>

    <div class="brand">
      <div class="brand__mark"></div>
      <p class="brand__name"><span>Tails of Glee</span><span>Pet Photography</span></p>
    </div>

    <div class="contact contact--person">
      <p class="contact__name">Marcus Fenwick</p>
      <p class="contact__role">Photographer</p>
      <p>0437 560914</p>
      <p>marcus@kfstudio.com.au</p>
      <p>www.tailsofglee.com.au</p>
    </div>

    <div class="contact-divider"></div>

    <div class="contact contact--address">
      <p class="contact__label">Studio address</p>
      <p>27 Wren Close, Marrowdale 6015</p>
      <p class="contact__label">Postal Address</p>
      <p>9 Harlow St,</p>
      <p>East Marrowdale 6015</p>
    </div>
  </section>

  <section class="card card--back">
    <div class="brand">
      <div class="brand__mark"></div>
      <p class="brand__name"><span>Tails of Glee</span><span>Pet Photography</span></p>
    </div>
  </section>
</body>
</html>
```